Copper Lantern General Contracting Business Card

My company is a General Contracting and Handyman service based in a private community in Northeast Pennsylvania.
Our cliental is a mix of year round and seasonal homeowners
We pride ourselves i using new and innovative building techniques and always try to build with pride and integrity
Please check my website f(under construction) or a list of services and more information
The files below are my logo and my facebook business page profile pic

Industry/Entity Type

Building

Contact Information for Business Card

Copper Lantern General Contracting
Dale Hurst
Pine Hollow, Pennsylvania
570-555-0147
dale@cprlantern.com
www.cprlantern.com
www.facebook.com/copperlanterncontracting

```html
<!DOCTYPE html>
<html lang="en">
<head>
<meta charset="utf-8">
<title>Copper Lantern General Contracting – Business Card</title>
<link href="https://fonts.googleapis.com/css2?family=Roboto:wght@300;400;700;900&family=Open+Sans:wght@400;600;700&family=Oswald:wght@400&display=swap" rel="stylesheet">
<style>
  :root {
    --backdrop: #3a332f;
    --paper: #ffffff;
    --ink: #1a1a1a;
    --muted: #3c3c3c;
    --red: #d8261c;
    --orange: #ee7a12;
    --black: #111111;
    --mark-tint: rgba(0,0,0,0.05);
  }
  html, body {
    margin: 0;
    width: 1200px;
    height: 768px;
    overflow: hidden;
    background: var(--backdrop);
  }
  .canvas {
    position: relative;
    width: 1200px;
    height: 768px;
  }
  .card {
    position: absolute;
    top: 229px;
    width: 540px;
    height: 310px;
    background: var(--paper);
    overflow: hidden;
    box-shadow: 0 10px 30px rgba(0,0,0,0.45);
  }
  .card--front { left: 40px; }
  .card--back { left: 620px; }

  .brand {
    display: flex;
    align-items: center;
    gap: 8px;
    font-family: "Roboto", sans-serif;
    font-weight: 900;
    color: var(--red);
    white-space: nowrap;
  }
  .brand__square {
    display: inline-block;
    background: var(--black);
  }
  .card--front .brand {
    position: absolute;
    left: 50%;
    top: 50%;
    transform: translate(-50%, -50%);
    font-size: 30px;
  }
  .card--front .brand__square { width: 26px; height: 26px; }

  .faint-decor {
    position: absolute;
    left: 290px;
    top: 100px;
    width: 170px;
    height: 110px;
    background: radial-gradient(ellipse at center, var(--mark-tint), rgba(0,0,0,0) 70%);
  }

  .card__bands {
    position: absolute;
    inset: 0;
  }
  .company {
    position: absolute;
    left: 26px;
    top: 18px;
    font-family: "Roboto", sans-serif;
    color: var(--ink);
  }
  .company__name {
    margin: 0;
    font-size: 30px;
    font-weight: 900;
    line-height: 1;
  }
  .company__trade {
    margin: 2px 0 0;
    font-size: 19px;
    font-weight: 300;
  }
  .person {
    position: absolute;
    left: 26px;
    top: 80px;
    font-family: "Open Sans", sans-serif;
    color: var(--ink);
  }
  .person__name { font-weight: 700; font-size: 13px; }
  .person__role { font-size: 10px; margin-left: 6px; }
  .contacts {
    position: absolute;
    left: 26px;
    top: 102px;
    margin: 0;
    padding: 0;
    list-style: none;
    font-family: "Open Sans", sans-serif;
    font-size: 10.5px;
    color: var(--muted);
    line-height: 15px;
  }
  .contacts li { display: flex; align-items: center; gap: 7px; }
  .contacts svg { width: 9px; height: 9px; fill: var(--red); flex: none; }
  .card--back .brand {
    position: absolute;
    right: 24px;
    top: 116px;
    font-size: 22px;
  }
  .card--back .brand__square { width: 18px; height: 18px; }
  .services {
    position: absolute;
    right: 22px;
    bottom: 10px;
    margin: 0;
    text-align: right;
    font-family: "Oswald", sans-serif;
    font-size: 12.5px;
    line-height: 15px;
    color: var(--paper);
    letter-spacing: 0.2px;
  }
</style>
</head>
<body>
<main class="canvas">

  <section class="card card--front" aria-label="Card front">
    <div class="brand"><span class="brand__square"></span>Copper Lantern</div>
  </section>

  <section class="card card--back" aria-label="Card back">
    <svg class="card__bands" viewBox="0 0 540 310" width="540" height="310" aria-hidden="true">
      <defs>
        <linearGradient id="band" x1="0" y1="1" x2="1" y2="0">
          <stop offset="0" stop-color="#d8261c"/>
          <stop offset="1" stop-color="#f08a14"/>
        </linearGradient>
      </defs>
      <path d="M0,197 C140,252 330,257 540,167 L540,310 L0,310 Z" fill="url(#band)"/>
      <path d="M0,186 C150,241 330,246 540,156 L540,161 C330,251 150,248 0,191 Z" fill="#111"/>
      <path d="M0,192 C150,248 330,252 540,162 L540,165 C330,255 150,252 0,195 Z" fill="#9a9a9a"/>
    </svg>
    <div class="faint-decor" role="img" aria-label="Faint tool motif in light grey"></div>

    <header class="company">
      <h1 class="company__name">Copper Lantern</h1>
      <p class="company__trade">General Contracting</p>
    </header>

    <div class="person">
      <span class="person__name">Dale Hurst</span><span class="person__role">Managing Director</span>
    </div>

    <ul class="contacts">
      <li><svg viewBox="0 0 10 10"><path d="M2 0h2l1 3-1.5 1a6 6 0 0 0 2.5 2.5L7 5l3 1v2c0 1-1 2-2 2A8 8 0 0 1 0 2c0-1 1-2 2-2z"/></svg>570-555-0147</li>
      <li><svg viewBox="0 0 10 10"><path d="M0 2h10v6H0z M0 2l5 3.5L10 2" stroke="#fff" stroke-width="0.8"/></svg>dale@cprlantern.com</li>
      <li><svg viewBox="0 0 10 10"><circle cx="5" cy="5" r="5"/></svg>www.cprlantern.com</li>
      <li><svg viewBox="0 0 10 10"><path d="M5 0a3.5 3.5 0 0 1 3.5 3.5C8.5 6 5 10 5 10S1.5 6 1.5 3.5A3.5 3.5 0 0 1 5 0z"/></svg>Pine Hollow, Pennsylvania</li>
      <li><svg viewBox="0 0 10 10"><rect width="10" height="10" rx="1.5"/></svg>/copperlanterncontracting</li>
    </ul>

    <div class="brand"><span class="brand__square"></span>Copper Lantern</div>

    <p class="services">
      Tile • Electrical<br>
      Plumbing • Drywall<br>
      Decks • Renovations<br>
      Kitchens • Bathrooms<br>
      Basements Extensions • Garages<br>
      Structural Repairs • Hardwood/Laminate Flooring
    </p>
  </section>

</main>
</body>
</html>
```